Wine and retail website for a high-end resort community

We are introducing a line of quality wines in the resort community of Harrowmere, Massachusetts, USA. The site will detail information about the wine, and online store connected to and external government approved shipper for wine, and additional non-alcoholic retail merchandise sales.

We are planning the site to be driven off the Squarespace platform so I do not believe coding is necessary initially; however, the ability to do sop would be helpful if needed.

Attached are the images/files we have available so far. Please feel free to use stock images in your design.

Target Market(s)

Wine enthusiasts in the resort community of Martha’s Vineyard Massachusetts

Industry/Entity Type

Wine

Number of Pages Required

4 page

Font styles to use
Sans Serif

Requirements
Must have
• Home page, about page, wine page, e-commerce page, retail merchandise page. I recently came across brelmorcellars.com and really like the look and layout of their pages if that helps
Nice to have
• A short wine/Martha’s Vineyard related video on the home page

```html
<!DOCTYPE html>
<html lang="en">
<head>
<meta charset="utf-8">
<title>Harrowmere Estates</title>
<link href="https://fonts.googleapis.com/css2?family=Libre+Caslon+Text:wght@400;700&family=Roboto:wght@400;500;700&display=swap" rel="stylesheet">
<style>
:root{
  --wine:#8b1e35;
  --wine-dark:#6e1628;
  --gold:#e0b000;
  --ink:#222;
  --text:#555;
  --muted:#8a8a8a;
  --nav:#ececec;
  --soft:#f4f4f4;
  --footer:#2a2a2a;
  --white:#fff;
}
*{box-sizing:border-box;margin:0;padding:0}
html,body{width:1200px;height:4566px;overflow:hidden}
body{position:relative;font-family:"Roboto",Arial,sans-serif;color:var(--ink);background:var(--white)}
.abs{position:absolute}
.serif{font-family:"Libre Caslon Text",Georgia,serif}
.btn{position:absolute;display:flex;align-items:center;justify-content:center;background:var(--wine);color:var(--white);font-weight:700;font-size:14px;border-radius:26px;letter-spacing:.3px}
.section-title{position:absolute;left:0;width:1200px;text-align:center;font-family:"Libre Caslon Text",Georgia,serif;font-size:40px;color:var(--ink);letter-spacing:.5px}
.section-title::after{content:"";display:block;width:74px;height:4px;background:var(--gold);margin:6px auto 0}
.intro{position:absolute;left:140px;width:920px;text-align:center;font-size:16px;line-height:27px;color:#444}
.circle-btn{position:absolute;width:50px;height:50px;border-radius:50%;background:var(--white);box-shadow:0 3px 12px rgba(0,0,0,.15);display:flex;align-items:center;justify-content:center}
.nav a{position:absolute;top:0;font-size:14px;color:var(--ink);text-decoration:none;line-height:57px;font-weight:500}
.photo{position:absolute}
.product-title{position:absolute;font-size:25px;font-weight:700;color:var(--ink)}
.product-text{position:absolute;width:490px;font-size:14px;line-height:26px;color:var(--text)}
.price{position:absolute;font-size:38px;color:var(--ink)}
.price s{font-size:16px;color:var(--muted);margin-left:14px}
.stars{position:absolute;color:var(--gold);font-size:22px;letter-spacing:2px}
.feature{position:absolute;width:300px;text-align:center;color:var(--white)}
.feature .icon{width:82px;height:82px;border-radius:50%;border:2px solid var(--white);margin:0 auto 26px;display:flex;align-items:center;justify-content:center}
.feature h3{font-size:17px;font-weight:700;margin-bottom:12px}
.feature p{font-size:14px;line-height:25px}
.blog-side{position:absolute;left:810px;width:258px}
.blog-side h4{font-size:20px;line-height:29px;font-weight:700;color:var(--ink);margin-bottom:10px}
.blog-side p{font-size:14px;line-height:24px;color:var(--muted);text-align:justify}
.footer{position:absolute;left:0;top:4159px;width:1200px;height:407px;background:var(--footer);color:var(--white)}
.footer h5{position:absolute;font-size:16px;font-weight:700}
.footer .link{position:absolute;font-size:14px;display:flex;align-items:center;gap:16px}
.footer .link i{width:14px;height:14px;border-radius:50%;background:var(--gold);display:inline-block}
.contact-row{position:absolute;left:514px;display:flex;align-items:center;gap:18px;font-size:14px;line-height:20px}
.contact-row .ic{width:36px;height:36px;border-radius:50%;border:1.5px solid #ddd;display:flex;align-items:center;justify-content:center;flex:none}
.social{position:absolute;top:4395px;width:36px;height:36px;border-radius:50%;border:1.5px solid #ddd}
</style>
</head>
<body>

<!-- Header -->
<header>
  <div class="abs" style="left:110px;top:46px;width:144px;text-align:right">
    <div style="font-size:11px;color:#777;letter-spacing:.5px">CALL US:</div>
    <div style="font-size:16px;font-weight:700;margin-top:6px">+1 (555) 014 2290</div>
  </div>
  <div class="circle-btn" style="left:274px;top:44px">
    <svg width="18" height="18" viewBox="0 0 24 24"><path fill="#8b1e35" d="M6.6 10.8a15.1 15.1 0 0 0 6.6 6.6l2.2-2.2c.3-.3.7-.4 1-.2 1.1.4 2.3.6 3.6.6.6 0 1 .4 1 1V20c0 .6-.4 1-1 1A17 17 0 0 1 3 4c0-.6.4-1 1-1h3.5c.6 0 1 .4 1 1 0 1.3.2 2.5.6 3.6.1.3 0 .7-.2 1z"/></svg>
  </div>
  <div class="abs serif" style="left:470px;top:48px;width:260px;text-align:center;font-size:28px;line-height:30px;color:#222">Harrowmere<div style="font-size:11px;letter-spacing:6px;line-height:16px;margin-top:6px">ESTATES</div></div>
  <div class="circle-btn" style="left:896px;top:44px">
    <svg width="18" height="18" viewBox="0 0 24 24"><path fill="#8b1e35" d="M3 4h3l2.6 10h9.6L21 7H8M9 19a1.5 1.5 0 1 0 0 .1M17 19a1.5 1.5 0 1 0 0 .1" stroke="#8b1e35" stroke-width="1.5"/></svg>
  </div>
  <div class="abs" style="left:965px;top:46px">
    <div style="font-size:11px;color:#777;letter-spacing:.5px">YOUR CART:</div>
    <div style="font-size:16px;font-weight:700;margin-top:6px">0 ITEMS - $0.00</div>
  </div>
  <nav class="nav abs" style="left:0;top:135px;width:1200px;height:57px;background:var(--nav)">
    <a style="left:318px;color:var(--gold)">HOME</a>
    <a style="left:420px">ABOUT</a>
    <a style="left:527px">WINE</a>
    <a style="left:622px">SHOP</a>
    <a style="left:721px">RETAIL MERCHANDISE</a>
  </nav>
</header>

<!-- Hero -->
<section>
  <div class="photo" role="img" aria-label="Sunset over vineyard rows with wine bottles, glasses, grapes and a barrel on a wooden table" style="left:0;top:192px;width:1200px;height:614px;background:linear-gradient(180deg,#4a3550 0%,#b5614a 30%,#e09a5a 45%,#5d6a2c 62%,#3f4a1e 80%,#8a5a34 100%)"></div>
  <svg class="abs" style="left:0;top:770px" width="1200" height="40" viewBox="0 0 1200 40" preserveAspectRatio="none"><path fill="#fff" d="M0 28 L80 18 L160 30 L260 16 L380 26 L480 14 L600 28 L720 18 L820 30 L940 16 L1060 26 L1200 14 V40 H0Z"/></svg>
  <h1 class="abs serif" style="left:112px;top:390px;font-size:42px;font-weight:400;color:var(--white)">HARROWMERE</h1>
  <p class="abs" style="left:112px;top:456px;width:480px;font-size:17px;line-height:29px;color:var(--white)">Lorem ipsum dolor sit amet, consectetur adipiscing elit sed do eiusmod tempor incididuntea.</p>
  <div class="btn" style="left:112px;top:532px;width:133px;height:48px">SHOP NOW</div>
</section>

<!-- Products -->
<section>
  <h2 class="section-title" style="top:912px">OUR PRODUCTS</h2>
  <p class="intro" style="top:994px">Lorem ipsum dolor sit amet, consectetur adipiscing elit, sed do eiusmod tempor incididunt ut labore et dolore magna aliqua. Ut enim ad minim veniam, quis nostrud exercitation ullamco laboris nisi ut aliquip ex ea commodo consequat. Duis aute irure dolor in reprehenderit in voluptate velit esse cillum dolorea.</p>

  <div class="photo" role="img" aria-label="Friends toasting with red wine at an outdoor table" style="left:112px;top:1126px;width:410px;height:410px;border-radius:50%;border:12px solid var(--wine);background:linear-gradient(160deg,#e8d6b0,#b89a6a 55%,#6d5a3c)"></div>
  <div class="photo" role="img" aria-label="Bottle of red wine with a white label" style="left:417px;top:1120px;width:110px;height:428px;border-radius:28px 28px 10px 10px;background:linear-gradient(90deg,#2a0d12,#4a1a22 50%,#1f090d)"></div>
  <h3 class="product-title" style="left:600px;top:1178px">CABERNET SAUVIGNON</h3>
  <p class="product-text" style="left:600px;top:1228px">Lorem ipsum dolor sit amet, consectetur adipiscing elit, sed do eiusmod tempor incididunt ut labore et dolore magna aliqua. Ut enim ad minim veniam, quis nostrud exercitationea.</p>
  <div class="price" style="left:600px;top:1320px">$140.00<s>$200.00</s></div>
  <div class="stars" style="left:600px;top:1372px">★★★★★</div>
  <div class="btn" style="left:600px;top:1431px;width:133px;height:49px">SHOP NOW</div>

  <h3 class="product-title" style="left:112px;top:1671px">CHARDONNAY</h3>
  <p class="product-text" style="left:112px;top:1722px">Lorem ipsum dolor sit amet, consectetur adipiscing elit, sed do eiusmod tempor incididunt ut labore et dolore magna aliqua. Ut enim ad minim veniam, quis nostrud exercitationea.</p>
  <div class="price" style="left:112px;top:1813px">$140.00<s>$200.00</s></div>
  <div class="stars" style="left:112px;top:1865px">★★★★★</div>
  <div class="btn" style="left:112px;top:1925px;width:133px;height:48px">SHOP NOW</div>
  <div class="photo" role="img" aria-label="Couple harvesting grapes among the vines" style="left:679px;top:1622px;width:408px;height:408px;border-radius:50%;border:12px solid var(--gold);background:linear-gradient(160deg,#9bb35a,#5f7a2c 55%,#8a6a3a)"></div>
  <div class="photo" role="img" aria-label="Bottle of white wine with a white label" style="left:674px;top:1601px;width:111px;height:447px;border-radius:28px 28px 10px 10px;background:linear-gradient(90deg,#2c3a18,#5a6a2e 50%,#26320f)"></div>
</section>

<!-- About -->
<section class="abs" style="left:0;top:2149px;width:1200px;height:702px;background:var(--soft)">
  <h2 class="section-title" style="top:66px">ABOUT US</h2>
  <p class="intro" style="top:150px">Lorem ipsum dolor sit amet, consectetur adipiscing elit, sed do eiusmod tempor incididunt ut labore et dolore magna aliqua. Ut enim ad minim veniam, quis nostrud exercitation ullamco laboris nisi ut aliquip ex ea commodo consequat. Duis aute irure dolor in reprehenderit in voluptate velit esse cillum dolorea.</p>
  <div class="photo" role="img" aria-label="Video: wine being poured into a glass in the vineyard" style="left:112px;top:266px;width:487px;height:356px;border:6px solid var(--white);border-radius:8px;box-shadow:0 4px 16px rgba(0,0,0,.12);background:linear-gradient(140deg,#c9c35a,#7e8a2a 55%,#4c5a1c)">
    <svg class="abs" style="left:206px;top:141px" width="62" height="62" viewBox="0 0 62 62"><circle cx="31" cy="31" r="30" fill="rgba(255,255,255,.35)"/><circle cx="31" cy="31" r="17" fill="#fff"/><path d="M27 24 L37 31 L27 38Z" fill="#e0b000"/></svg>
  </div>
  <div class="abs" style="left:667px;top:296px;width:422px;font-size:14px;line-height:26px;color:var(--text);text-align:justify">
    <p style="margin-bottom:10px">Lorem ipsum dolor sit amet, consectetur adipiscing elit, sed do eiusmod tempor incididunt ut labore et dolore magna aliqua. Ut enim ad minim veniam, quis nostrud exercitation ullamco laboris nisi ut aliquip ex ea commodo consequat. Duis aute irure dolor in reprehenderitea.</p>
    <p>Lorem ipsum dolor sit amet, consectetur adipiscing elit, sed do eiusmod tempor incididunt ut labore et dolore magna aliqua ut enim ad minimea.</p>
  </div>
  <div class="btn" style="left:667px;top:539px;width:150px;height:49px">LEARN MORE</div>
</section>

<!-- Why choose us -->
<section class="abs" style="left:0;top:2851px;width:1200px;height:461px;background:linear-gradient(180deg,var(--wine-dark),var(--wine) 40%)">
  <h2 class="section-title" style="top:64px;color:var(--white)">WHY CHOOSE US</h2>
  <div class="feature" style="left:109px;top:158px">
    <div class="icon"><svg width="40" height="40" viewBox="0 0 40 40" fill="none" stroke="#fff" stroke-width="1.6"><circle cx="20" cy="16" r="10"/><path d="M10 16h20M20 6v20M14 30h12M20 26v4"/></svg></div>
    <h3>LOREM IPSUM DOLOR</h3>
    <p>Lorem ipsum dolor sit amet, consectetur adipiscing elit, sed do eiusmod tempor incididunt ut labore et dolore magna aliqua. Ut enim ad minim veniea.</p>
  </div>
  <div class="feature" style="left:449px;top:158px">
    <div class="icon"><svg width="40" height="40" viewBox="0 0 40 40" fill="none" stroke="#fff" stroke-width="1.6"><circle cx="20" cy="20" r="14"/><rect x="14" y="12" width="12" height="16" rx="3"/><path d="M14 20h12"/></svg></div>
    <h3>LOREM IPSUM DOLOR</h3>
    <p>Lorem ipsum dolor sit amet, consectetur adipiscing elit, sed do eiusmod tempor incididunt ut labore et dolore magna aliqua. Ut enim ad minim veniea.</p>
  </div>
  <div class="feature" style="left:791px;top:158px">
    <div class="icon"><svg width="40" height="40" viewBox="0 0 40 40" fill="none" stroke="#fff" stroke-width="1.6"><path d="M12 8h6v6l2 4v14h-10V18l2-4z"/><path d="M24 12h8l-1 8a3 3 0 0 1-6 0z M28 23v8M25 31h6"/></svg></div>
    <h3>LOREM IPSUM DOLOR</h3>
    <p>Lorem ipsum dolor sit amet, consectetur adipiscing elit, sed do eiusmod tempor incididunt ut labore et dolore magna aliqua. Ut enim ad minim veniea.</p>
  </div>
</section>

<!-- Blog -->
<section>
  <h2 class="section-title" style="top:3418px">LATEST BLOG</h2>
  <div class="photo" role="img" aria-label="Glasses of red wine and grapes on a barrel in a sunny vineyard" style="left:117px;top:3516px;width:480px;height:308px;background:linear-gradient(160deg,#d9c56a,#8a8a2c 50%,#4a3a1c)"></div>
  <h4 class="abs" style="left:117px;top:3846px;width:480px;font-size:22px;line-height:31px;font-weight:700">Lorem ipsum dolor sit amet, consect adipiscing elit commodo</h4>
  <p class="abs" style="left:117px;top:3914px;width:470px;font-size:14px;line-height:24px;color:var(--muted)">Lorem ipsum dolor sit amet, consectetur adipiscing elit, sed do eiusmod tempor incididunt ut labore et dolore magna aliqua ut enim ad minim veniam, quis nostrud.</p>
  <div class="btn" style="left:117px;top:4007px;width:135px;height:48px">READ MORE</div>

  <div class="photo" role="img" aria-label="Two glasses of white wine clinking" style="left:608px;top:3516px;width:183px;height:168px;background:linear-gradient(150deg,#6b5a48,#2d241c)"></div>
  <div class="blog-side" style="top:3516px"><h4>Lorem ipsum dolor sit amet consea</h4><p>Lorem ipsum dolor sit amet, consectetur adipiscing elit, sed do eiusmod tempor incididunt ut labore et dolorea.</p></div>
  <div class="photo" role="img" aria-label="Red wine poured into a glass beside cheese" style="left:608px;top:3700px;width:183px;height:169px;background:linear-gradient(150deg,#c9bfb2,#7a2a2a 60%,#3a1a14)"></div>
  <div class="blog-side" style="top:3700px"><h4>Lorem ipsum dolor sit amet consea</h4><p>Lorem ipsum dolor sit amet, consectetur adipiscing elit, sed do eiusmod tempor incididunt ut labore et dolorea.</p></div>
  <div class="photo" role="img" aria-label="Two glasses of red wine on a candlelit dinner table" style="left:608px;top:3885px;width:183px;height:170px;background:linear-gradient(150deg,#d88a3a,#5a1e18 55%,#1e0e0a)"></div>
  <div class="blog-side" style="top:3885px"><h4>Lorem ipsum dolor sit amet consea</h4><p>Lorem ipsum dolor sit amet, consectetur adipiscing elit, sed do eiusmod tempor incididunt ut labore et dolorea.</p></div>
</section>

<!-- Footer -->
<footer class="footer">
  <div class="abs serif" style="left:100px;top:178px;width:200px;text-align:center;font-size:26px;line-height:30px;color:var(--white)">Harrowmere<div style="font-size:11px;letter-spacing:6px;line-height:16px;margin-top:6px">ESTATES</div></div>

  <h5 style="left:319px;top:78px">OTHER LINKS</h5>
  <div class="link" style="left:319px;top:120px"><i></i>Home</div>
  <div class="link" style="left:319px;top:164px"><i></i>About</div>
  <div class="link" style="left:319px;top:208px"><i></i>Wine</div>
  <div class="link" style="left:319px;top:252px"><i></i>Shop</div>
  <div class="link" style="left:319px;top:296px"><i></i>Retail Merchandise</div>

  <h5 style="left:514px;top:78px">CONTACT US</h5>
  <div class="contact-row" style="top:116px"><span class="ic"><svg width="14" height="16" viewBox="0 0 14 18"><path fill="#fff" d="M7 0a7 7 0 0 0-7 7c0 5 7 11 7 11s7-6 7-11a7 7 0 0 0-7-7zm0 9.5A2.5 2.5 0 1 1 7 4.5a2.5 2.5 0 0 1 0 5z"/></svg></span><span>Harrowmere Estates<br>Alder Creek, CA</span></div>
  <div class="contact-row" style="top:172px"><span class="ic"><svg width="14" height="12" viewBox="0 0 16 12"><path fill="#fff" d="M0 0h16v12H0z"/><path d="M0 0l8 6 8-6" stroke="#2a2a2a" stroke-width="1.5" fill="none"/></svg></span><span>info@harrowmere.com</span></div>
  <div class="contact-row" style="top:222px"><span class="ic"><svg width="14" height="14" viewBox="0 0 24 24"><path fill="#fff" d="M6.6 10.8a15.1 15.1 0 0 0 6.6 6.6l2.2-2.2c.3-.3.7-.4 1-.2 1.1.4 2.3.6 3.6.6.6 0 1 .4 1 1V20c0 .6-.4 1-1 1A17 17 0 0 1 3 4c0-.6.4-1 1-1h3.5c.6 0 1 .4 1 1 0 1.3.2 2.5.6 3.6.1.3 0 .7-.2 1z"/></svg></span><span>+1 (555) 014 2290</span></div>

  <h5 style="left:800px;top:78px">SIGN UP TO OUR NEWSLETTER</h5>
  <div class="abs" style="left:800px;top:122px;width:287px;padding-bottom:8px;border-bottom:1.5px solid #ccc;font-size:13px">Email</div>
  <div class="btn" style="left:800px;top:165px;width:136px;height:48px;background:var(--gold)">SUBSCRIBE</div>
  <span class="social" aria-label="Social link" style="left:800px;top:236px;background:var(--wine);border-color:var(--wine)"></span>
  <span class="social" aria-label="Social link" style="left:843px;top:236px"></span>
  <span class="social" aria-label="Social link" style="left:886px;top:236px"></span>
  <span class="social" aria-label="Social link" style="left:929px;top:236px"></span>

  <div class="abs" style="left:112px;top:350px;width:976px;height:1px;background:#555"></div>
  <div class="abs" style="left:0;top:370px;width:1200px;text-align:center;font-size:13px">© 2024 HARROWMERE &nbsp;| &nbsp;All Rights Reserved</div>
  <div class="abs" style="left:906px;top:370px;display:flex;gap:5px" aria-label="Accepted payment methods">
    <span style="width:33px;height:18px;background:#fff;border-radius:2px"></span>
    <span style="width:33px;height:18px;background:#fff;border-radius:2px"></span>
    <span style="width:33px;height:18px;background:#fff;border-radius:2px"></span>
    <span style="width:33px;height:18px;background:#fff;border-radius:2px"></span>
    <span style="width:33px;height:18px;background:#fff;border-radius:2px"></span>
  </div>
</footer>

</body>
</html>
```